Graphic design of labels for scented candles

Following a change in our team structure, a deadline was put in place and the brief changed.
We need a beautiful label for our candles, one that sticks *all around the glass*. Must obviously include our logo as well as the description of the perfume.
The clientele is mainly female, between 35 and 65 years old, of a classic nature.
Brand values:
Feminine
Warm-joyful
Sophisticated-elegant
Eco-friendly, pet-friendly
Natural
Inspires confidence.
The idea is to have something different, the final appearance must be elegant and refined, which will be your challenge given the shape.

What we need:
- changeable colors
- small transparent elements which can be printed on a gold or silver paper background (example: logo, frame, elements, etc.)

- the logo (black or very dark gray) must be present + text "vegetable candle", then the perfume and below:
vegetable wax - handcrafted"
I am attaching a picture of our current labels to the files.
For the size I'll let you manage.
These labels can also be assigned to derived products such as room fragrances, pillow mists, etc.
The brand targets the middle class and above.
For the fonts I leave the choice to you.
Thank you and good luck to all !

Update: there is no longer a cat's head as a background shape, you have free choice.
THANKS

Target Market(s)

Women aged 35 to 65

Industry/Entity Type

Industrie du Parfum

Colors
00AB8E
00BBA5
67D7C9
C6EFE9
E9F9F6
59FF00
82FF00
B8FF75
E3FFCB
F4FFEA
FFF300
FFF600
FEFA6F
FFFEC7
FFFEE8
FFC000
F8CF3A
FAE287
FDF2CF
FEFAEE
F0912C
F2A743
F7CA91
FBE8D2
FDF5EE
EE7325
F08F49
F5BC92
FAE3D3
FDF4ED
EB3D1F
EC4F4E
F09395
F8D3D4
FCEDEE
E54698
E96AAD
F1A4CE
F9D9EA
FCEFF6
A7469A
B969AE
D3A5CF
EDDBEB
F8F0F9
6B429C
8869AF
B7A5CE
E3DAEB
F3F0F8

Requirements
Must have
• modifiable colors - small transparent elements which can be printed on a gold or silver paper background (example: frame, elements, etc.) - the logo (black or very dark gray) must be present + text "vegetable candle, then the perfume and below: vegetable wax - handcrafted"
Nice to have
• Elements that could be made transparent (logo text frame) to be able to edit on gold papers and give a luxurious appearance
Should not have
• no childish appearance.

```html
<!DOCTYPE html>
<html lang="en">
<head>
<meta charset="utf-8">
<title>Velours – Cannelle douce candle labels</title>
<link rel="stylesheet" href="https://fonts.googleapis.com/css2?family=Great+Vibes&family=Montserrat:wght@400;500;600&display=swap">
<style>
  :root {
    --page-bg: #ffffff;
    --gold-deep: #a77c45;
    --gold-mid: #d2ab6c;
    --gold-light: #f4dfa6;
    --gold-pale: #fbefc9;
    --gold-warm: #d8b173;
    --panel: #ffffff;
    --ink: #1c1c1c;
    --ink-soft: #3a3a3a;
    --badge: #e1251b;
  }
  * { box-sizing: border-box; margin: 0; padding: 0; }
  html, body {
    width: 1200px;
    height: 1200px;
    overflow: hidden;
    background: var(--page-bg);
  }
  .sheet {
    width: 1200px;
    height: 1200px;
    display: flex;
    align-items: center;
    justify-content: center;
    gap: 60px;
  }
  .label {
    position: relative;
    overflow: hidden;
    background: linear-gradient(90deg,
      var(--gold-deep) 0%,
      var(--gold-mid) 40%,
      var(--gold-light) 70%,
      var(--gold-pale) 80%,
      var(--gold-warm) 100%);
  }
  .label--wrap { width: 500px; height: 468px; }
  .label--round { width: 520px; height: 520px; border-radius: 50%; }

  .label-panel {
    position: absolute;
    background: var(--panel);
    border-radius: 78px 10px 92px 0;
    display: flex;
    flex-direction: column;
    align-items: center;
    text-align: center;
    color: var(--ink);
    font-family: "Montserrat", sans-serif;
  }
  .label--wrap .label-panel { left: 93px; top: 88px; width: 300px; height: 330px; }
  .label--round .label-panel { left: 99px; top: 110px; width: 298px; height: 330px; }

  .perfume-name {
    font-family: "Great Vibes", cursive;
    font-size: 50px;
    line-height: 1;
    font-weight: 400;
    margin-top: 34px;
  }
  .product-type {
    font-size: 11px;
    letter-spacing: 2px;
    font-weight: 500;
    margin-top: 18px;
  }
  .brand {
    margin-top: 52px;
    display: flex;
    align-items: center;
    gap: 10px;
  }
  .brand-dot {
    width: 14px;
    height: 14px;
    border-radius: 50%;
    background: var(--ink);
  }
  .brand-name {
    font-size: 34px;
    font-weight: 600;
    letter-spacing: 1px;
    color: var(--ink);
  }
  .brand-site {
    font-size: 7px;
    font-weight: 600;
    letter-spacing: 0.5px;
    margin-top: 10px;
    color: var(--ink-soft);
  }
  .origin-badge {
    width: 7px;
    height: 7px;
    background: var(--badge);
    margin-top: 6px;
  }
  .product-claim {
    font-size: 12px;
    font-weight: 400;
    margin-top: 8px;
    color: var(--ink);
  }
</style>
</head>
<body>
  <main class="sheet">
    <section class="label label--wrap" aria-label="Wrap-around label">
      <div class="label-panel">
        <h1 class="perfume-name">Cannelle douce</h1>
        <p class="product-type">VEGETABLE CANDLE</p>
        <div class="brand"><span class="brand-dot"></span><span class="brand-name">Velours</span></div>
        <p class="brand-site">veloursbougie.com</p>
        <span class="origin-badge"></span>
        <p class="product-claim">vegetable wax - handcrafted</p>
      </div>
    </section>

    <section class="label label--round" aria-label="Round label">
      <div class="label-panel">
        <h2 class="perfume-name">Cannelle douce</h2>
        <p class="product-type">VEGETABLE CANDLE</p>
        <div class="brand"><span class="brand-dot"></span><span class="brand-name">Velours</span></div>
        <p class="brand-site">veloursbougie.com</p>
        <span class="origin-badge"></span>
        <p class="product-claim">vegetable wax - handcrafted</p>
      </div>
    </section>
  </main>
</body>
</html>
```